Brightline Villas Estepona listings flyer

Brightline Villas Estepona are a specialist estate agency focussed solely on selling modern and contemporary homes.

We need an A4 folded flyer to be designed so that Brightline Villas Estepona can leaflet drop all of the modern homes for sale in our area to generate new instructions / listings. We need to engage with owners of those types of homes by posting this marketing material through their letter boxes in the hope that they see our funky and modern design and decide to call us about our services to sell their home, if for sale.

We would like to see sharp lines and a modern design (see our logo for style and colour scheme), with lots of white spaces and using photos which can blend in to the background to provide a powerful and impacting image to set us aside from any other direct mail leaflets which may be in their post box. It needs to show

* Quality
* Style
* Modern and forward thinking in design and outlook
* Professionalism

Front page
Top:
Logo of Brightline Villas Estepona.
Helping you sell your modern home. It’s all we do!

4 property photos in a grid position

Bottom banner
If you are thinking of selling, read on…

INSIDE LEFT & RIGHT (DOUBLE PAGE POSSIBLY BLANK WHITE BACKGROUND)
Title: Use Brightline Villas Estepona – the specialist modern homes agency to sell your home

We bring an exciting and dynamic mix of modern marketing with good old fashioned service to guarantee only the most qualified clients will be viewing your home (use online marketing image)

Marketing packages include stylish online brochures, professional photography, stunning drone video footage, informative video walk thru’s and unique floor plans (use drone and floor plan images)

Targeted social media campaigns focusing on international clientele actively looking to buy property in southern Spain (use social media image)

Bespoke, powerful advertising packages enable worldwide exposure for both online and traditional channels to market. We can be as discreet or as visible as you want us to be to sell your home

During our 20 years on the Costa del Sol, we have built up an enviable network of collaborating agents meaning you only have to instruct one expert real estate agent, Brightline Villas Estepona, to gain maximum exposure for your home

BACK PAGE

If you want service that matches the value of your home, contact us today for a private, personalised consultation. Brightline Villas Estepona. It’s all we do.

Suite 14
Torrenova Office Park
Calle Los Almendros
Valdemoro, Marbella

Tel: +34 952 418 306
Mobil y Whatsapp: +34 677 342 815
Email: info@brightlinevillasestepona.example
www.brightlinevillasestepona.example

Target Market(s)

Wealthy property owners of contemporary and modern homes who are looking to sell their home

Industry/Entity Type

Real Estate Agent

Font styles to use
Serif
Sans Serif

Colors
606060
e7e7e7
f5f5f5

Requirements
Must have
• Classy, professional, modern design with the ability to stand out from other leaflet drops / direct mail in letter box
Nice to have
• straight lines to border photos
• Maybe extend the lines further than they should so it has the look of an architects plan
• Blend in images to white background in the middle open double page
Should not have
• Lots of different colours

```html
<!DOCTYPE html>
<html lang="en">
<head>
<meta charset="utf-8">
<title>Brightline Villas Estepona – Listings Flyer</title>
<link rel="stylesheet" href="https://fonts.googleapis.com/css2?family=Montserrat:wght@300;400;600;700;800&family=Lora:ital,wght@0,400;0,600;1,400&display=swap">
<style>
:root{
  --ink:#606060;
  --ink-dark:#3f3f3f;
  --rule:#e7e7e7;
  --paper:#ffffff;
  --mist:#f5f5f5;
  --stage:#d9d9d9;
  --sky-1:#9cc3e6;
  --sky-2:#dfe9f2;
  --villa:#eef1f3;
  --pool:#5aa6cf;
  --accent:#2f6fa8;
}
*{box-sizing:border-box;margin:0;padding:0}
html,body{width:1200px;height:2368px;overflow:hidden}
body{background:var(--stage);font-family:'Montserrat',sans-serif;color:var(--ink);position:relative}

.page{position:absolute;background:var(--paper);overflow:hidden;box-shadow:0 2px 10px rgba(0,0,0,.12)}
.sheet-front{left:340px;top:40px;width:520px;height:735px}
.spread{left:80px;width:1040px;height:735px}
.spread-inside{top:810px}
.spread-outer{top:1590px}
.half{position:absolute;top:0;width:520px;height:735px}
.half-left{left:0}
.half-right{left:520px}
.fold{position:absolute;left:519px;top:0;width:2px;height:100%;background:linear-gradient(90deg,rgba(0,0,0,.06),rgba(0,0,0,0))}

.photo{position:absolute}
.photo-villa{background:linear-gradient(180deg,var(--sky-1) 0%,var(--sky-2) 45%,var(--villa) 70%,#b9c4cc 100%)}
.photo-pool{background:linear-gradient(180deg,var(--sky-1) 0%,var(--villa) 55%,var(--pool) 100%)}
.photo-dusk{background:linear-gradient(180deg,#5f7d9c 0%,#c7d3de 55%,#e9ecef 100%)}

.brand{position:absolute;display:flex;align-items:center;gap:8px}
.brand-mark{width:14px;height:14px;background:var(--ink)}
.brand-name{font-weight:600;font-size:11px;letter-spacing:2px;text-transform:uppercase;color:var(--ink)}

.cover-brand{top:18px;left:0;width:100%;justify-content:center}
.cover-hero{left:0;top:52px;width:520px;height:250px}
.plan-line{position:absolute;background:var(--ink);opacity:.55}
.sale-box{position:absolute;left:26px;top:280px;width:150px;height:118px;background:var(--ink-dark);color:#fff;padding:14px 14px}
.sale-box .sale-kicker{font-size:12px;font-weight:700;letter-spacing:1px;line-height:1.1}
.sale-box .sale-word{font-size:30px;font-weight:800;letter-spacing:1px;line-height:1}
.sale-box .sale-phone{margin-top:12px;font-size:11px;font-weight:600;letter-spacing:.5px}
.tagline{position:absolute;left:200px;top:318px;width:300px}
.tagline .lead{font-size:21px;font-weight:300;line-height:1.15;color:var(--ink)}
.tagline .punch{font-size:22px;font-weight:800;color:var(--ink-dark);margin-top:4px}
.thumb-row{position:absolute;left:26px;top:420px;width:468px;height:140px;display:flex;gap:10px}
.thumb-row .photo{position:relative;flex:1;height:100%}
.cover-band{position:absolute;left:0;bottom:0;width:100%;height:70px;background:var(--ink);color:#fff;display:flex;align-items:center;justify-content:center;font-size:13px;letter-spacing:1px}
.cover-band strong{font-weight:800;margin:0 5px}
.cover-web{position:absolute;left:0;bottom:80px;width:100%;text-align:center;font-size:9px;letter-spacing:1.5px;color:var(--ink)}

.inside-title{position:absolute;left:34px;top:46px;width:230px}
.inside-title .eyebrow{font-size:15px;font-weight:700;letter-spacing:1px;text-transform:uppercase;color:var(--ink-dark);line-height:1.2}
.inside-title .sub{font-family:'Lora',serif;font-style:italic;font-size:15px;line-height:1.3;margin-top:6px}
.inside-title .rule{width:60px;height:3px;background:var(--ink);margin-top:12px}
.body-copy{font-family:'Lora',serif;font-size:11px;line-height:1.55;color:var(--ink)}
.copy-left{position:absolute;left:34px;top:230px;width:220px}
.copy-center{position:absolute;left:370px;top:470px;width:300px;text-align:center}
.copy-center .head{font-family:'Montserrat',sans-serif;font-size:12px;font-weight:700;letter-spacing:1px;color:var(--ink-dark);margin-bottom:6px}
.copy-center p+p{margin-top:8px}
.social-block{position:absolute;left:812px;top:230px;width:200px}
.social-block .head{font-size:15px;font-weight:700;letter-spacing:1px;color:var(--ink-dark);line-height:1.2;text-transform:uppercase;margin-bottom:10px}
.inside-brand{top:40px;right:34px}
.hex-layer{position:absolute;left:0;top:0}

.back-brand{top:30px;left:34px}
.back-hero{left:0;top:80px;width:520px;height:230px}
.back-copy{position:absolute;left:34px;top:336px;width:452px;font-family:'Lora',serif;font-size:13px;line-height:1.55;color:var(--ink)}
.back-copy strong{font-family:'Montserrat',sans-serif;font-weight:700;color:var(--ink-dark)}
.contact{position:absolute;left:34px;top:450px;width:452px;display:flex;gap:34px}
.contact ul{list-style:none;font-size:11px;line-height:1.9;color:var(--ink)}
.contact li{display:flex;align-items:center;gap:8px}
.contact svg{flex:none}
.back-band{position:absolute;left:0;bottom:0;width:100%;height:70px;background:var(--ink)}
</style>
</head>
<body>

<!-- Front cover -->
<section class="page sheet-front" aria-label="Front cover">
  <div class="brand cover-brand"><span class="brand-mark"></span><span class="brand-name">Brightline Villas Estepona</span></div>
  <div class="photo photo-villa cover-hero" role="img" aria-label="Modern white villa with glass balconies under a blue sky"></div>
  <div class="plan-line" style="left:0;top:52px;width:520px;height:1px"></div>
  <div class="plan-line" style="left:20px;top:40px;width:1px;height:540px"></div>
  <div class="plan-line" style="left:500px;top:40px;width:1px;height:540px"></div>
  <div class="sale-box">
    <div class="sale-kicker">PROPERTIES</div>
    <div class="sale-kicker">FOR</div>
    <div class="sale-word">SALE</div>
    <div class="sale-phone">+34 952 418 306</div>
  </div>
  <div class="tagline">
    <div class="lead">Helping you<br>sell your modern home.</div>
    <div class="punch">IT’S ALL WE DO!</div>
  </div>
  <div class="thumb-row">
    <div class="photo photo-pool" role="img" aria-label="Contemporary villa with infinity pool"></div>
    <div class="photo photo-villa" role="img" aria-label="White modern house facade"></div>
    <div class="photo photo-dusk" role="img" aria-label="Modern home lit at dusk"></div>
  </div>
  <div class="plan-line" style="left:0;top:570px;width:520px;height:1px"></div>
  <div class="cover-web">www.brightlinevillasestepona.example</div>
  <div class="cover-band">If you are <strong>THINKING</strong> of <strong>SELLING</strong>, read on...</div>
</section>

<!-- Inside spread -->
<section class="page spread spread-inside" aria-label="Inside spread">
  <svg class="hex-layer" width="1040" height="735" viewBox="0 0 1040 735" aria-hidden="false">
    <defs>
      <linearGradient id="g-online" x1="0" y1="0" x2="1" y2="1"><stop offset="0" stop-color="#c9d9ea"/><stop offset="1" stop-color="#f2f5f8"/></linearGradient>
      <linearGradient id="g-drone" x1="0" y1="0" x2="0" y2="1"><stop offset="0" stop-color="#a9c7e3"/><stop offset="1" stop-color="#eef2f5"/></linearGradient>
      <linearGradient id="g-plan" x1="0" y1="0" x2="1" y2="1"><stop offset="0" stop-color="#eeeeee"/><stop offset="1" stop-color="#d5d8db"/></linearGradient>
      <linearGradient id="g-house" x1="0" y1="0" x2="0" y2="1"><stop offset="0" stop-color="#6d8fb3"/><stop offset="1" stop-color="#dfe6ec"/></linearGradient>
      <linearGradient id="g-social" x1="0" y1="0" x2="1" y2="1"><stop offset="0" stop-color="#2f4f7a"/><stop offset="1" stop-color="#8fb0d1"/></linearGradient>
    </defs>
    <line x1="300" y1="60" x2="760" y2="60" stroke="#606060" stroke-width="1" opacity=".4"/>
    <line x1="300" y1="445" x2="760" y2="445" stroke="#606060" stroke-width="1" opacity=".4"/>
    <polygon role="img" aria-label="Floor plan drawing" points="780,240 730,326 630,326 580,240 630,154 730,154" fill="url(#g-plan)" stroke="#fff" stroke-width="4"/>
    <polygon role="img" aria-label="Online marketing screen image" points="660,200 590,321 450,321 380,200 450,79 590,79" fill="url(#g-online)" stroke="#fff" stroke-width="5"/>
    <polygon role="img" aria-label="Drone flying over property" points="450,340 405,418 315,418 270,340 315,262 405,262" fill="url(#g-drone)" stroke="#fff" stroke-width="4"/>
    <polygon role="img" aria-label="Modern house at dusk" points="220,610 165,705 55,705 0,610 55,515 165,515" fill="url(#g-house)" stroke="#fff" stroke-width="4"/>
    <polygon role="img" aria-label="Smartphone showing social media apps" points="1040,610 985,705 875,705 820,610 875,515 985,515" fill="url(#g-social)" stroke="#fff" stroke-width="4"/>
  </svg>
  <div class="half half-left">
    <div class="inside-title">
      <div class="eyebrow">Use Brightline Villas Estepona</div>
      <div class="sub">– the specialist modern homes agency to sell your home</div>
      <div class="rule"></div>
    </div>
    <p class="body-copy copy-left">We bring an exciting and dynamic mix of modern marketing with good old fashioned service to guarantee only the most qualified clients will be viewing your home.</p>
  </div>
  <div class="fold"></div>
  <div class="copy-center body-copy">
    <div class="head">MARKETING PACKAGES</div>
    <p>Include stylish online brochures, professional photography, stunning drone video footage, informative video walk thru’s and unique floor plans.</p>
    <p>During our 20 years on the Costa del Sol, we have built up an enviable network of collaborating agents meaning you only have to instruct one expert real estate agent, Brightline Villas Estepona, to gain maximum exposure for your home.</p>
  </div>
  <div class="brand inside-brand"><span class="brand-mark"></span><span class="brand-name">Brightline Villas Estepona</span></div>
  <div class="social-block">
    <div class="head">Targeted<br>social media<br>campaigns</div>
    <p class="body-copy">Focusing on international clientele actively looking to buy property in southern Spain.</p>
  </div>
</section>

<!-- Outer spread: back page and front cover -->
<section class="page spread spread-outer" aria-label="Back page and front cover">
  <div class="half half-left">
    <div class="brand back-brand"><span class="brand-mark"></span><span class="brand-name">Brightline Villas Estepona</span></div>
    <div class="photo photo-pool back-hero" role="img" aria-label="Contemporary villa with pool terrace"></div>
    <div class="plan-line" style="left:20px;top:66px;width:1px;height:260px"></div>
    <div class="plan-line" style="left:0;top:80px;width:520px;height:1px"></div>
    <p class="back-copy">If you want service that matches the value of your home, contact us today for a private, personalised consultation. <strong>Brightline Villas Estepona. It’s all we do.</strong></p>
    <div class="contact">
      <ul>
        <li><svg width="12" height="14" viewBox="0 0 12 14"><path d="M6 0a5 5 0 0 1 5 5c0 4-5 9-5 9S1 9 1 5a5 5 0 0 1 5-5z" fill="#606060"/><circle cx="6" cy="5" r="2" fill="#fff"/></svg>Suite 14</li>
        <li><span style="width:12px"></span>Torrenova Office Park</li>
        <li><span style="width:12px"></span>Calle Los Almendros</li>
        <li><span style="width:12px"></span>Valdemoro, Marbella</li>
      </ul>
      <ul>
        <li><svg width="12" height="12" viewBox="0 0 12 12"><path d="M2 1l2.5-.5 1.5 3-1.5 1a6 6 0 0 0 3 3l1-1.5 3 1.5L11 10c-5 1-10-4-9-9z" fill="#606060"/></svg>Tel: +34 952 418 306</li>
        <li><svg width="12" height="12" viewBox="0 0 12 12"><rect x="3" y="0" width="6" height="12" rx="1" fill="#606060"/><rect x="4" y="1.5" width="4" height="8" fill="#fff"/></svg>Mobil y Whatsapp: +34 677 342 815</li>
        <li><svg width="12" height="10" viewBox="0 0 12 10"><rect x="0" y="0" width="12" height="10" fill="#606060"/><path d="M0 0l6 5 6-5" stroke="#fff" fill="none"/></svg>info@brightlinevillasestepona.example</li>
        <li><svg width="12" height="12" viewBox="0 0 12 12"><circle cx="6" cy="6" r="5.5" fill="none" stroke="#606060"/><path d="M0.5 6h11M6 .5c-3 3-3 8 0 11M6 .5c3 3 3 8 0 11" stroke="#606060" fill="none"/></svg>www.brightlinevillasestepona.example</li>
      </ul>
    </div>
    <div class="back-band"></div>
  </div>
  <div class="fold"></div>
  <div class="half half-right">
    <div class="brand cover-brand"><span class="brand-mark"></span><span class="brand-name">Brightline Villas Estepona</span></div>
    <div class="photo photo-villa cover-hero" role="img" aria-label="Modern white villa with glass balconies under a blue sky"></div>
    <div class="plan-line" style="left:0;top:52px;width:520px;height:1px"></div>
    <div class="plan-line" style="left:20px;top:40px;width:1px;height:540px"></div>
    <div class="plan-line" style="left:500px;top:40px;width:1px;height:540px"></div>
    <div class="sale-box">
      <div class="sale-kicker">PROPERTIES</div>
      <div class="sale-kicker">FOR</div>
      <div class="sale-word">SALE</div>
      <div class="sale-phone">+34 952 418 306</div>
    </div>
    <div class="tagline">
      <div class="lead">Helping you<br>sell your modern home.</div>
      <div class="punch">IT’S ALL WE DO!</div>
    </div>
    <div class="thumb-row">
      <div class="photo photo-pool" role="img" aria-label="Contemporary villa with infinity pool"></div>
      <div class="photo photo-villa" role="img" aria-label="White modern house facade"></div>
      <div class="photo photo-dusk" role="img" aria-label="Modern home lit at dusk"></div>
    </div>
    <div class="plan-line" style="left:0;top:570px;width:520px;height:1px"></div>
    <div class="cover-web">www.brightlinevillasestepona.example</div>
    <div class="cover-band">If you are <strong>THINKING</strong> of <strong>SELLING</strong>, read on...</div>
  </div>
</section>

</body>
</html>
```